DL Flyer and magnet design

I am in need of a new flyer design to show some offers on each side. First side Water filtration. Second side Heat pump hot water. I will attach an existing design from a previous flyer/magnet. I have also got some information to go on the flyer and images/logo.

Side 1: Water Filtration Solutions
Coral Ridge Pipeworks and Heating
Fresh, Clean Water for Every Tap

Water Filtration Solutions
1️⃣ High Flow Water Filtration
Starting from just $550!

2️⃣ Whole House Water Filtration
Enjoy pure water throughout your home – starting from $1800!

3️⃣ Whole House Water Filtration with UV Lamp (Perfect for rainwater systems)
Get the ultimate filtration – starting from $3000!

🎁 FREE BRAVO COOLER
With every water filtration system or referral!

📞 Call us today: 0491 837 254
🌐 Visit our website: www.coralridgeph.example.au

💧 Better water, better life. Call now for a free quote!

Side 2: Heat Pump Hot Water Systems
Energy-Efficient Hot Water Solutions

Heat Pump Hot Water Systems
🌟 Rebates Available!
Save big with government incentives on energy-efficient hot water systems.

💼 All Major Makes, Models, and Sizes
We supply and install trusted brands to suit your household’s needs.

💳 Interest-Free Finance Options
Upgrade now and pay later with flexible payment plans.

🎁 FREE BRAVO COOLER
With every heat pump system or referral!

💧 Upgrade to energy-efficient hot water and save!

Please include on the flyer. Valid until 30/6/2-25 Images are for illustrative purposes only and may not represent the exact product or service provided

```html
<!DOCTYPE html>
<html lang="en">
<head>
<meta charset="utf-8">
<title>Coral Ridge Pipeworks and Heating – DL Flyers</title>
<link rel="stylesheet" href="https://fonts.googleapis.com/css2?family=Poppins:wght@400;500;600;700;800;900&family=Oswald:wght@500;600&display=swap">
<style>
:root{
  --stage:#5b6466;
  --navy:#2e3590;
  --orange:#f5821f;
  --yellow:#fbb91a;
  --white:#ffffff;
  --ink:#444650;
  --rule:#333333;
}
*{box-sizing:border-box;margin:0;padding:0}
html,body{width:1200px;height:1200px;overflow:hidden;background:var(--stage);font-family:'Poppins',sans-serif}
.flyer{position:absolute;top:155px;width:433px;height:890px;background:var(--white);overflow:hidden;box-shadow:0 2px 4px rgba(0,0,0,.35)}
.flyer--water{left:124px}
.flyer--heat{left:624px}

/* brand */
.brand{position:absolute;left:0;right:0;top:0;height:110px;display:flex;align-items:center;justify-content:center;gap:12px}
.brand__mark{width:34px;height:34px;background:var(--navy)}
.brand__name{font-weight:600;color:var(--navy);font-size:20px;line-height:1.1}

/* hero */
.hero{position:absolute;left:0;right:0;background:var(--navy);color:var(--white)}
.water-hero{top:110px;height:183px;text-align:center}
.water-hero h1{font-weight:700;font-size:41px;line-height:1.08;margin-top:24px}
.hl{color:var(--yellow)}
.water-hero p{font-size:17px;line-height:1.25;margin-top:10px}
.heat-hero{top:115px;height:281px}
.heat-hero__photo{position:absolute;right:0;top:0;width:169px;height:100%;background:linear-gradient(90deg,var(--navy) 0%,#5a4a7a 35%,#8a4a3a 70%,#a24a36 100%)}
.heat-hero h1{position:absolute;left:42px;top:26px;font-weight:700;font-size:39px;line-height:1.08}
.heat-hero p{position:absolute;left:42px;top:170px;font-size:17.5px;line-height:1.2}

.band{position:absolute;left:0;right:0;background:linear-gradient(90deg,var(--orange),var(--yellow) 55%,var(--orange));color:var(--white);font-weight:700;display:flex;align-items:center;justify-content:center;font-size:21px}

/* product rows */
.product{position:absolute;left:39px;width:351px}
.product__img{position:absolute;background:linear-gradient(180deg,#c9ccd2,#6d727c);border-radius:4px}
.product__name{position:absolute;left:104px;color:var(--navy);font-weight:700;font-size:16px;line-height:1.2}
.product__name small{display:block;font-weight:400;color:#222;font-size:10px;line-height:1.4}
.product__note{position:absolute;left:249px;width:120px;font-size:10px;color:var(--ink);line-height:1.3}
.price{position:absolute;left:249px;width:90px;height:35px}
.price svg{position:absolute;left:0;top:0}
.price span{position:absolute;left:16px;right:0;top:0;bottom:0;display:flex;align-items:center;justify-content:center;font-family:'Oswald',sans-serif;font-weight:500;color:var(--white);font-size:28px}
.price sup{font-size:12px;margin-top:-12px}
.rule{position:absolute;left:39px;width:351px;height:1px;background:var(--rule)}

/* free banner */
.free{position:absolute;left:32px;top:682px;width:370px;height:62px;border-radius:6px;background:linear-gradient(90deg,var(--navy) 35%,var(--orange))}
.free__word{position:absolute;left:14px;top:2px;font-weight:800;font-size:52px;color:var(--white);line-height:58px;letter-spacing:-1px}
.free__tag{position:absolute;left:164px;top:-5px;width:88px;height:55px;background:var(--yellow);border-radius:4px;text-align:center;color:var(--navy);font-weight:800}
.free__tag b{display:block;font-size:22px;line-height:28px;margin-top:5px}
.free__tag i{display:block;font-style:normal;font-size:13px;line-height:15px}
.free__text{position:absolute;left:260px;top:7px;color:var(--white);font-size:12px;line-height:1.3}

/* contact */
.call{position:absolute;display:flex;align-items:center;gap:7px;color:var(--navy);font-weight:800;font-size:22px}
.call__pill{border:2px solid var(--navy);border-radius:14px;padding:0 4px 0 5px;line-height:22px;display:flex;align-items:center;gap:6px}
.call__icon{width:20px;height:20px;border-radius:50%;background:var(--orange);display:flex;align-items:center;justify-content:center}
.web{position:absolute;height:25px;border-radius:13px;border:2px solid var(--navy);background:linear-gradient(90deg,var(--white) 38%,var(--orange) 38%,var(--yellow) 80%,var(--orange));display:flex;align-items:center;font-size:13px;font-weight:600;z-index:2}
.web__label{color:var(--navy);padding-left:12px;width:38%}
.web__globe{width:21px;height:21px;border-radius:50%;background:var(--navy);display:flex;align-items:center;justify-content:center;margin-left:-11px}
.web__url{color:var(--white);padding-left:9px;font-weight:500}
.foot{position:absolute;left:0;right:0;bottom:0;background:var(--navy);color:var(--white);text-align:center}

/* feature boxes */
.feature{position:absolute;left:40px;width:351px;border:1.5px solid #333;border-radius:4px;text-align:center;font-size:10.5px;color:var(--ink);line-height:1.3;padding:0 16px}
.feature__pill{position:absolute;left:63px;width:305px;height:23px;border-radius:12px;background:linear-gradient(90deg,var(--navy),#6b4a7e 55%,var(--orange));color:var(--white);font-weight:700;font-size:15.5px;display:flex;align-items:center;justify-content:center;z-index:2}
</style>
</head>
<body>

<section class="flyer flyer--water">
  <div class="brand"><div class="brand__mark"></div><div class="brand__name">Coral Ridge<br>Pipeworks and Heating</div></div>

  <div class="hero water-hero">
    <h1>Water Filtration<br><span class="hl">Solutions</span></h1>
    <p>Coral Ridge Pipeworks and Heating<br>Fresh, Clean Water for Every Tap</p>
  </div>
  <div class="band" style="top:293px;height:39px">Water Filtration Solutions</div>

  <div class="product" style="top:332px;height:108px">
    <div class="product__img" role="img" aria-label="High flow cartridge water filter" style="left:34px;top:7px;width:20px;height:92px"></div>
    <div class="product__name" style="top:24px">High Flow<br>Water<br>Filtration</div>
    <div class="product__note" style="top:35px">Starting from just</div>
    <div class="price" style="top:50px">
      <svg width="90" height="35"><polygon points="0,0 7,0 16,35 9,35" fill="#2e3590"/><polygon points="9,0 88,0 88,35 18,35" fill="#f5821f"/></svg>
      <span><sup>$</sup>550</span>
    </div>
  </div>
  <div class="rule" style="top:440px"></div>

  <div class="product" style="top:440px;height:110px">
    <div class="product__img" role="img" aria-label="Whole house twin filter system" style="left:7px;top:25px;width:71px;height:64px"></div>
    <div class="product__name" style="top:35px">Whole House<br>Water<br>Filtration</div>
    <div class="product__note" style="top:14px">Enjoy pure water throughout your home starting from</div>
    <div class="price" style="top:67px">
      <svg width="90" height="35"><polygon points="0,0 7,0 16,35 9,35" fill="#2e3590"/><polygon points="9,0 88,0 88,35 18,35" fill="#f5821f"/></svg>
      <span><sup>$</sup>1800</span>
    </div>
  </div>
  <div class="rule" style="top:550px"></div>

  <div class="product" style="top:550px;height:124px">
    <div class="product__img" role="img" aria-label="Twin filter system with UV lamp" style="left:2px;top:27px;width:78px;height:72px"></div>
    <div class="product__name" style="top:12px">Whole House<br>Water Filtration<br>with UV Lamp<small>(Perfect for<br>rainwater systems)</small></div>
    <div class="product__note" style="top:14px">Get the ultimate filtration starting from</div>
    <div class="price" style="top:63px;width:94px">
      <svg width="94" height="35"><polygon points="0,0 7,0 16,35 9,35" fill="#2e3590"/><polygon points="9,0 92,0 92,35 18,35" fill="#f5821f"/></svg>
      <span><sup>$</sup>3000</span>
    </div>
  </div>

  <div class="free">
    <div class="free__word">FREE</div>
    <div class="free__tag"><b>BRAVO</b><i>COOLER</i></div>
    <div class="free__text">With every water<br>filtration system<br>or referral!</div>
  </div>

  <div class="call" style="left:32px;top:758px">
    <div class="call__pill">CALL US TODAY
      <div class="call__icon"><svg width="12" height="12" viewBox="0 0 24 24"><path fill="#fff" d="M6.6 10.8a15 15 0 006.6 6.6l2.2-2.2c.3-.3.7-.4 1-.2 1.1.4 2.3.6 3.6.6.6 0 1 .4 1 1V20c0 .6-.4 1-1 1A17 17 0 013 4c0-.6.4-1 1-1h3.5c.6 0 1 .4 1 1 0 1.3.2 2.5.6 3.6.1.3 0 .7-.2 1z"/></svg></div>
    </div>
    <span>0491 837 254</span>
  </div>
  <div class="web" style="left:32px;top:794px;width:370px">
    <span class="web__label">Visit our website</span>
    <span class="web__globe"><svg width="14" height="14" viewBox="0 0 24 24" fill="none" stroke="#fff" stroke-width="1.6"><circle cx="12" cy="12" r="10"/><ellipse cx="12" cy="12" rx="4.5" ry="10"/><path d="M2 12h20M4 7h16M4 17h16"/></svg></span>
    <span class="web__url">www.coralridgeph.example.au</span>
  </div>
  <div class="foot" style="height:84px;padding-top:26px">
    <div style="font-weight:700;font-size:15.5px;line-height:1.2">Better water, better life.</div>
    <div style="font-size:15px;line-height:1.3">Call now for a free quote!</div>
  </div>
</section>

<section class="flyer flyer--heat">
  <div class="brand" style="height:115px"><div class="brand__mark"></div><div class="brand__name">Coral Ridge<br>Pipeworks and Heating</div></div>

  <div class="hero heat-hero">
    <div class="heat-hero__photo" role="img" aria-label="Heat pump hot water unit installed beside a brick wall"></div>
    <h1>Heat Pump<br><span class="hl">Hot Water</span><br>Systems</h1>
    <p>Coral Ridge<br>Pipeworks and Heating<br>Energy-Efficient<br>Hot Water Solutions</p>
  </div>
  <div class="band" style="top:396px;height:54px">Heat Pump Hot Water Systems</div>

  <div class="feature__pill" style="top:478px">Rebates Available!</div>
  <div class="feature" style="top:489px;height:45px;padding-top:12px">Save big with government incentives on energy-efficient hot water systems.</div>

  <div class="feature__pill" style="top:548px">All Major Makes, Models, and Sizes</div>
  <div class="feature" style="top:560px;height:45px;padding-top:12px">We supply and install trusted brands to suit your household’s needs.</div>

  <div class="feature__pill" style="top:618px">Interest-Free Finance Options</div>
  <div class="feature" style="top:630px;height:38px;padding-top:15px">Upgrade now and pay later with flexible payment plans.</div>

  <div class="feature__pill" style="top:681px">FREE BRAVO COOLER</div>
  <div class="feature" style="top:692px;height:39px;padding-top:18px">With every heat pump system or referral!</div>

  <div class="call" style="left:37px;top:764px">
    <div class="call__pill">CALL US TODAY
      <div class="call__icon"><svg width="12" height="12" viewBox="0 0 24 24"><path fill="#fff" d="M6.6 10.8a15 15 0 006.6 6.6l2.2-2.2c.3-.3.7-.4 1-.2 1.1.4 2.3.6 3.6.6.6 0 1 .4 1 1V20c0 .6-.4 1-1 1A17 17 0 013 4c0-.6.4-1 1-1h3.5c.6 0 1 .4 1 1 0 1.3.2 2.5.6 3.6.1.3 0 .7-.2 1z"/></svg></div>
    </div>
    <span>0491 837 254</span>
  </div>
  <div class="web" style="left:37px;top:799px;width:371px">
    <span class="web__label">Visit our website</span>
    <span class="web__globe"><svg width="14" height="14" viewBox="0 0 24 24" fill="none" stroke="#fff" stroke-width="1.6"><circle cx="12" cy="12" r="10"/><ellipse cx="12" cy="12" rx="4.5" ry="10"/><path d="M2 12h20M4 7h16M4 17h16"/></svg></span>
    <span class="web__url">www.coralridgeph.example.au</span>
  </div>
  <div class="foot" style="height:78px;padding-top:28px;font-size:15px">Upgrade to energy-efficient hot water and save!</div>
</section>

</body>
</html>
```